Security Officer Training Certifications POSTCARD

We need Post Card Design
-Front and Back
-In Compliance with TORLEN HUB for upload!
-For Oversized and Jumbo Size Cards (torlen hubs)
Our Company:
www.ashworthmaplebrookinstitute.org (FOR IDEAS)
We provide Corporate Security Officer/Criminal Justice/Police Tactics Training for Private Companies that have a security department and officers.
We provide:
Handcuffing certifications
Pepper Spray
Compliance Training
Instructor Training
California Guard Card
Our Card to display powerful image for a Security Officer Department
Traits in Pic and Deigns
VALUE
COMPETITIVE EDGE
PROFESSIONAL GROWTH
QUALITY
PROFICIENT/EFFECTIVE SECURITY OFFICERS
TACTICAL OFFICERS
PROFESSIONALISM
EXPERTS
INDUSTRY LEADERS
READINESS
FRONT DESIGN TO BE VERY CATCH AND ATTRACTIVE!
-Please put the images of lawn enforcement, security guards, public safety department in the FRONT
BACK OF THE CARD DESIGN
-Please put our Services/Menu, CREATIVE and CATCHY, in columns and with vivid colors.

```html
<!DOCTYPE html>
<html lang="en">
<head>
<meta charset="utf-8">
<title>Ashworth Maplebrook – Security Officer Training Postcards</title>
<link href="https://fonts.googleapis.com/css2?family=Source+Sans+3:wght@400;600;700&display=swap" rel="stylesheet">
<style>
  :root {
    --maroon: #4a1a1c;
    --maroon-deep: #3a1214;
    --cream: #f8ecc8;
    --label: #f1dfae;
    --ink: #3d1416;
    --white: #ffffff;
    --stage: #f6efdc;
    --badge-silver: #c9ccd2;
    --badge-gold: #d9b45a;
  }
  * { box-sizing: border-box; margin: 0; padding: 0; }
  html, body { width: 1200px; height: 800px; overflow: hidden; }
  body {
    background: var(--stage);
    font-family: "Source Sans 3", Arial, sans-serif;
    position: relative;
  }

  /* ---------- Card shells ---------- */
  .postcard { position: absolute; background: var(--white); overflow: hidden; box-shadow: 0 2px 6px rgba(0,0,0,.18); }
  .postcard--contact { left: 30px; top: 30px; width: 700px; height: 460px; }
  .postcard--services { left: 430px; top: 310px; width: 740px; height: 470px; }

  .photo { position: absolute; }

  /* ---------- Contact card ---------- */
  .contact-panel { position: absolute; left: 0; top: 0; width: 400px; height: 460px; }
  .contact-panel__hero { position: absolute; left: 0; top: 0; width: 400px; height: 152px; background: var(--maroon); }
  .contact-panel__hero .photo {
    left: 70px; top: 14px; width: 316px; height: 124px;
    border: 3px solid var(--label);
    background: linear-gradient(180deg, #6f7a6a 0%, #3f4a5a 55%, #2c2f3a 100%);
  }
  .brand-badge {
    position: absolute; display: flex; flex-direction: column; align-items: center; justify-content: center;
    text-align: center; color: var(--ink); font-weight: 700; line-height: 1.05;
  }
  .brand-badge__mark {
    border-radius: 50%; background: var(--badge-silver); border: 3px solid var(--badge-gold);
    display: flex; align-items: center; justify-content: center; text-align: center;
  }
  .contact-panel__hero .brand-badge { left: 12px; top: 28px; }
  .contact-panel__hero .brand-badge__mark { width: 96px; height: 96px; font-size: 12px; padding: 8px; }

  .traits {
    position: absolute; left: 0; top: 152px; width: 400px; height: 140px; background: var(--cream);
    display: flex; flex-direction: column; justify-content: center; align-items: center;
    color: var(--ink); font-weight: 700; font-size: 15.5px; line-height: 1.5; text-transform: uppercase; text-align: center;
  }
  .contact-info {
    position: absolute; left: 0; top: 292px; width: 400px; height: 104px; background: var(--maroon);
    color: var(--white); text-align: center; padding-top: 12px;
  }
  .contact-info__phone { font-size: 21px; font-weight: 700; margin-bottom: 4px; }
  .contact-info__address { font-size: 11px; line-height: 1.25; }

  .contact-footer { position: absolute; left: 0; top: 396px; width: 400px; height: 64px; background: var(--white); }
  .partner-marks { position: absolute; left: 16px; top: 12px; display: flex; gap: 14px; align-items: center; }
  .partner-mark { width: 40px; height: 40px; }
  .partner-mark--square { background: #1f2430; border: 2px solid #4c6ea8; }
  .partner-mark--shield { background: #a6262a; border-radius: 50%; }
  .partner-mark--crest { background: #c8c8cc; border-radius: 4px; }
  .web-strip {
    position: absolute; left: 150px; top: 0; width: 250px; height: 64px; background: var(--maroon);
    clip-path: polygon(14% 0, 100% 0, 100% 100%, 0 100%);
    color: var(--white); font-size: 10.5px; font-weight: 600; display: flex; align-items: center; justify-content: flex-end; padding-right: 8px;
  }

  /* ---------- Services card ---------- */
  .services-photo {
    left: 0; top: 0; width: 390px; height: 270px;
    background: linear-gradient(160deg, #7a7462 0%, #4b4a45 45%, #1f2024 100%);
  }
  .services-menu {
    position: absolute; left: 0; top: 270px; width: 390px; height: 200px; background: var(--maroon);
    clip-path: polygon(0 14%, 100% 0, 100% 100%, 0 100%);
    padding: 40px 0 0 28px; color: var(--label);
  }
  .services-menu__label {
    display: inline-block; background: var(--label); color: var(--ink); font-weight: 700; font-size: 17px;
    padding: 1px 14px 1px 10px; margin-bottom: 8px;
  }
  .services-menu__list { list-style: none; font-size: 17px; line-height: 1.3; }
  .services-menu__list li { position: relative; padding-left: 22px; }
  .services-menu__list li::before { content: ""; position: absolute; left: 4px; top: 10px; width: 10px; height: 4px; background: var(--label); }

  .services-main { position: absolute; left: 390px; top: 0; width: 350px; height: 470px; }
  .range-band { position: absolute; left: 0; top: 0; width: 350px; height: 175px; background: var(--maroon); }
  .range-photo {
    left: 0; top: 0; width: 270px; height: 160px;
    background: linear-gradient(180deg, #3a3e40 0%, #6e7068 60%, #8d8a7c 100%);
  }
  .services-main .brand-badge { right: 12px; top: 28px; }
  .services-main .brand-badge__mark { width: 82px; height: 82px; font-size: 10.5px; padding: 6px; }
  .offer {
    position: absolute; left: 0; top: 175px; width: 350px; height: 215px; background: var(--cream);
    color: var(--ink); text-align: center; padding: 14px 10px 0 44px;
  }
  .offer__lead { font-size: 20px; font-weight: 700; line-height: 1.1; }
  .offer__headline { font-size: 24px; font-weight: 700; line-height: 1.08; margin: 2px 0 6px; }
  .offer__detail { font-size: 19px; font-weight: 600; line-height: 1.1; }
  .services-footer { position: absolute; left: 0; top: 390px; width: 350px; height: 80px; background: var(--white); border-top: 2px solid var(--maroon); }
  .services-footer .partner-marks { left: 70px; top: 14px; gap: 52px; }
  .services-footer .partner-mark { width: 48px; height: 48px; }

  .inset-photos { position: absolute; left: 290px; top: 318px; width: 150px; height: 152px; background: var(--maroon-deep); padding: 5px; }
  .inset-photo { position: relative; width: 100%; border: 2px solid var(--white); }
  .inset-photo--arrest { height: 66px; margin-bottom: 5px; background: linear-gradient(135deg, #b9b2a4 0%, #2e3340 70%); }
  .inset-photo--aid { height: 66px; background: linear-gradient(135deg, #8a6a55 0%, #d7d3cb 55%, #c23a2c 100%); }
</style>
</head>
<body>

<!-- Contact card -->
<section class="postcard postcard--contact" aria-label="Postcard with training values and contact details">
  <div class="contact-panel">
    <div class="contact-panel__hero">
      <div class="photo" role="img" aria-label="Group photo of graduates holding training certificates outdoors"></div>
      <div class="brand-badge">
        <div class="brand-badge__mark">Ashworth Maplebrook</div>
      </div>
    </div>

    <div class="traits">
      <p>Value | Competitive Edge</p>
      <p>Professional Growth | Quality</p>
      <p>Proficient/Effective Security Officers</p>
      <p>Tactical Officers | Professionalism</p>
      <p>Experts | Industry Leaders | Readiness</p>
    </div>

    <div class="contact-info">
      <p class="contact-info__phone">Call Now (555) 204-7719</p>
      <p class="contact-info__address">City of Halden and nearby cities<br>1280 Fairlane Ave<br>Halden, CA 90000</p>
    </div>

    <div class="contact-footer">
      <div class="partner-marks">
        <span class="partner-mark partner-mark--square"></span>
        <span class="partner-mark partner-mark--shield"></span>
        <span class="partner-mark partner-mark--crest"></span>
      </div>
      <div class="web-strip">www.ashworthmaplebrookinstitute.org</div>
    </div>
  </div>
</section>

<!-- Services card -->
<section class="postcard postcard--services" aria-label="Postcard listing training services">
  <div class="photo services-photo" role="img" aria-label="Group of trainees posing with a padded training shield and batons"></div>

  <div class="services-menu">
    <span class="services-menu__label">We provide:</span>
    <ul class="services-menu__list">
      <li>Handcuffing certifications</li>
      <li>Pepper Spray</li>
      <li>Compliance Training</li>
      <li>Instructor Training</li>
      <li>California Guard Card</li>
    </ul>
  </div>

  <div class="services-main">
    <div class="range-band">
      <div class="photo range-photo" role="img" aria-label="Firing range with an officer aiming at silhouette targets"></div>
      <div class="brand-badge">
        <div class="brand-badge__mark">Ashworth Maplebrook</div>
      </div>
    </div>

    <div class="offer">
      <p class="offer__lead">We provide</p>
      <h1 class="offer__headline">Corporate Security Officer<br>Criminal Justice<br>Police Tactics Training</h1>
      <p class="offer__detail">for Private Companies that have a security department and officers.</p>
    </div>

    <div class="services-footer">
      <div class="partner-marks">
        <span class="partner-mark partner-mark--square"></span>
        <span class="partner-mark partner-mark--shield"></span>
        <span class="partner-mark partner-mark--crest"></span>
      </div>
    </div>
  </div>

  <div class="inset-photos">
    <div class="inset-photo inset-photo--arrest" role="img" aria-label="Officers practising a handcuffing drill"></div>
    <div class="inset-photo inset-photo--aid" role="img" aria-label="First aid training in an office setting"></div>
  </div>
</section>

</body>
</html>
```